Workout book cover design: Looking for Simple Classic Cover

I need a book cover design for "The Steady Middle". A book on exercises to strengthen the pelvic floor. Basically it's exercises for your torso and hips. I want something tasteful and classic looking.

I like this book cover design: http://www.pagelorn-books.example/Calm-Starters-Gentle-Routines-Ease-ebook/dp/Q93KX7TM41/ref=sr_1_40?ie=UTF8&qid=2958173306&sr=8-40&keywords=exercise+books

Book Title: The Steady Middle
Description to go under title: I'm working on that now and will have ready by the end of the project. (The hidden world of pelvic floor training. Discover the best exercises for creating a strong core, hips and pelvis today!)

Target Market(s)

Mostly women 35-65 and men 60+

Industry/Entity Type

Health And Wellness

Requirements
Must have
• ebook dementions: 1536 x 2048 I think works for all the online publishing companies
• 8x10 for print
Nice to have
• I like this book cover design: http://www.pagelorn-books.example/Calm-Starters-Gentle-Routines-Ease-ebook/dp/Q93KX7TM41/ref=sr_1_40?ie=UTF8&qid=2958173306&sr=8-40&keywords=exercise+books
• This cover is also ok, but no shiny. http://www.pagelorn-books.example/Bedrock-Renew-The-Climb-Poise/dp/4827305519/ref=sr_1_2?ie=UTF8&qid=2958176642&sr=8-2&keywords=foundation+book
Should not have
• I do not like this cover, it's crowded. http://www.pagelorn-books.example/Gym-Drills-Selfweight-flexing-drills-ebook/dp/Q71RWJZNHE/ref=sr_1_2?ie=UTF8&qid=2958174418&sr=8-2&keywords=workout+books
• I do not want anyone on the cover making eye contact.

```html
<!DOCTYPE html>
<html lang="en">
<head>
<meta charset="UTF-8">
<title>The Steady Middle — Book Cover</title>
<link rel="stylesheet" href="https://fonts.googleapis.com/css2?family=Tinos:wght@400&display=swap">
<style>
  :root {
    --backdrop: #7d6a6a;
    --cover-light: #f3f1ea;
    --cover-mid: #e6e2d6;
    --cover-edge: #d2ccbc;
    --title-dark: #3a1f17;
    --title-orange: #d9772a;
    --body-text: #2e1c16;
    --sun-core: #f6c04a;
    --sun-glow: #e9901c;
    --sun-fade: rgba(233, 144, 28, 0);
  }
  * { margin: 0; padding: 0; box-sizing: border-box; }
  html, body {
    width: 1200px;
    height: 909px;
    overflow: hidden;
    background: var(--backdrop);
  }
  .canvas {
    position: relative;
    width: 1200px;
    height: 909px;
    display: flex;
    align-items: center;
    justify-content: center;
  }
  .cover {
    position: relative;
    width: 690px;
    height: 800px;
    background: radial-gradient(ellipse at 50% 45%, var(--cover-light) 0%, var(--cover-mid) 65%, var(--cover-edge) 100%);
    font-family: "Tinos", "Times New Roman", serif;
    text-align: center;
    color: var(--body-text);
  }
  .cover-title {
    position: absolute;
    top: 34px;
    left: 0;
    right: 0;
    font-weight: 400;
    line-height: 1;
    text-transform: uppercase;
  }
  .cover-title .title-top {
    display: block;
    font-size: 86px;
    color: var(--title-dark);
  }
  .cover-title .title-bottom {
    display: block;
    margin-top: 12px;
    font-size: 86px;
    color: var(--title-orange);
  }
  .cover-art {
    position: absolute;
    top: 228px;
    left: 50%;
    width: 390px;
    height: 390px;
    transform: translateX(-50%);
  }
  .cover-subtitle {
    position: absolute;
    top: 640px;
    left: 0;
    right: 0;
    font-size: 33px;
    line-height: 1.28;
  }
  .cover-author {
    position: absolute;
    top: 738px;
    left: 0;
    right: 0;
    font-size: 29px;
    text-transform: uppercase;
  }
</style>
</head>
<body>
  <main class="canvas">
    <article class="cover">
      <h1 class="cover-title">
        <span class="title-top">The Steady</span>
        <span class="title-bottom">Middle</span>
      </h1>

      <svg class="cover-art" viewBox="0 0 390 390" role="img"
           aria-label="Watercolour sun with a ring of sun-salutation yoga pose silhouettes around a hand-lettered centre">
        <defs>
          <radialGradient id="sunFill" cx="50%" cy="50%" r="50%">
            <stop offset="0%" stop-color="var(--sun-core)"/>
            <stop offset="45%" stop-color="var(--sun-glow)"/>
            <stop offset="100%" stop-color="var(--sun-fade)"/>
          </radialGradient>
        </defs>
        <circle cx="195" cy="195" r="195" fill="url(#sunFill)"/>
      </svg>

      <p class="cover-subtitle">A book on exercises to<br>strengthen the pelvic floor</p>
      <p class="cover-author">Author Name</p>
    </article>
  </main>
</body>
</html>
```